Logo and Packaging for Low Dose Full Spectrum Cannabis Extract Capsules - Pellet Co

Hi! I am hoping to get a logo and packaging design for low dose (2, 5, and 10mg) full spectrum cannabis extract capsules.

Overall we are going for a natural, healthy, earthy. clean, safe, trustworthy, environmentally friendly look and would love to use lots of natural colors like brown and green as well as white.

For the Pellet Co logo I would love to have something clean and simple, possibly involving a stylized capsule or plant/leaf.

The labels will be printed on 8x2" (203.2 x 50.8 mm) paper bands that will wrap around the 3.125" (79.4 mm) wide fronts and backs of white tin containers -the sides are 0.5625” (14.3 mm). There will be a 0.5" (12.7 mm) of overlap at the end of the band that will be covered by the adhesive.

Designs should include the following information:

Front:
- Pellet Co logo (not the main focus)
- X mg THC per capsule (final versions with 2, 5, and 10 and this should be relatively prominent. The capsules get darker as they get to higher strengths and it might be nice to represent that on the labels as well)
- Indica, Sativa, or Hybrid (maybe Purple for Indica, Green for Sativa, and a third color for Hybrid?)
- 15 Full Spectrum Cannabis Extract Capsules

Back:
- For adult use only. Keep away from children.
- This product has not been analyzed or evaluated by the NRB
- Ingredients: Olive oil, full spectrum cannabis extract, gelatin capsules
- Made in DC

Target Market(s)

Wealthy young professionals between 25 and 55, especially women, for the woman who has it all as a discreet and classy alternative to sleep aids, other herbal supplements, or a glass of Pinot noir

Font styles to use
Serif
Sans Serif
Other font styles liked:
• Garamond, Lucida Bright, Georgia, Goudy, Bangkok, Brooklyn, Sage

```html
<!DOCTYPE html>
<html lang="en">
<head>
<meta charset="utf-8">
<title>Pellet Co – Capsule Tin Bands</title>
<link rel="stylesheet" href="https://fonts.googleapis.com/css2?family=Open+Sans:wght@400;600;700;800&family=Oswald:wght@300&family=Roboto+Condensed:wght@700&display=swap">
<style>
  :root {
    --canvas: #b3b3b3;
    --paper: #ffffff;
    --ink: #111111;
    --card-rim: #6d6d6d;
    --seam-dark: #7a7a7a;
    --seam-light: #d8d8d8;
  }
  .band--indica { --tone: #46176f; --tone-deep: #5a2381; --tone-soft: #8a44f2; --accent: #5b22a6; }
  .band--sativa { --tone: #238a22; --tone-deep: #146c15; --tone-soft: #7cbd43; --accent: #238a22; }
  .band--hybrid { --tone: #ee7600; --tone-deep: #ea5c00; --tone-soft: #f59c3f; --accent: #ee7000; }

  * { box-sizing: border-box; margin: 0; padding: 0; }
  html, body { width: 1200px; height: 989px; overflow: hidden; }
  body { background: var(--canvas); font-family: "Open Sans", sans-serif; position: relative; }

  .band {
    position: absolute; left: 51px; width: 1090px; height: 272px;
    background: var(--tone); overflow: hidden;
  }
  .band--indica { top: 60px; }
  .band--sativa { top: 354px; }
  .band--hybrid { top: 652px; }

  .vertical { writing-mode: vertical-rl; position: absolute; white-space: nowrap; }
  .vertical--up { transform: rotate(180deg); }

  .band__edge { position: absolute; left: 0; top: 0; width: 22px; height: 100%; background: var(--paper); }
  .blank__label {
    left: 111px; top: 37px; font-family: "Oswald", sans-serif; font-weight: 300;
    font-size: 47px; line-height: 1; color: var(--tone-soft);
  }
  .seam {
    position: absolute; left: 237px; top: 0; width: 18px; height: 100%;
    background: linear-gradient(90deg, var(--seam-dark), var(--seam-light) 50%, var(--seam-dark));
  }
  .fold {
    position: absolute; left: 664px; top: 0; width: 26px; height: 100%;
    background: linear-gradient(90deg, var(--tone-deep), var(--tone));
  }

  /* back panel */
  .back__brand { left: 612px; top: 83px; font-size: 20px; font-weight: 800; color: var(--paper); line-height: 24px; }
  .back__molecule { position: absolute; left: 483px; top: 40px; width: 113px; height: 190px; background: linear-gradient(180deg, rgba(255,255,255,.16), rgba(255,255,255,.08)); border-radius: 6px; }
  .back__notice {
    left: 415px; top: 38px; height: 193px; width: 43px; padding: 5px 6px;
    background: var(--paper); border-radius: 7px; color: var(--accent);
    font-weight: 700; font-size: 11px; line-height: 15px;
  }
  .back__disclaimer { left: 373px; top: 40px; color: var(--paper); font-size: 11px; line-height: 14px; }
  .back__rule { position: absolute; top: 40px; width: 1px; height: 192px; background: rgba(255,255,255,.85); }
  .back__rule--a { left: 361px; }
  .back__rule--b { left: 313px; }
  .back__ingredients { left: 322px; top: 40px; color: var(--paper); font-size: 11px; line-height: 14px; font-weight: 600; }
  .back__origin-mark { position: absolute; left: 285px; top: 74px; width: 13px; height: 12px; background: var(--paper); border-radius: 2px; }
  .back__origin { left: 284px; top: 91px; color: var(--paper); font-size: 13px; font-weight: 700; line-height: 16px; }

  /* front panel */
  .front {
    position: absolute; left: 689px; top: 48px; width: 360px; height: 230px;
    background: var(--paper); border-top: 5px solid var(--card-rim); border-left: 5px solid var(--card-rim);
    border-radius: 14px 22px 0 0;
  }
  .front__brand { left: 734px; bottom: 22px; font-size: 25px; font-weight: 800; color: var(--accent); line-height: 28px; }
  .front__dose { left: 857px; bottom: 25px; font-size: 18px; font-weight: 700; color: var(--ink); line-height: 22px; }
  .front__strain {
    left: 916px; bottom: 25px; height: 125px; text-align: center;
    font-family: "Roboto Condensed", sans-serif; font-weight: 700; font-size: 40px; line-height: 40px;
    color: var(--accent); border-left: 2px solid var(--accent); border-right: 2px solid var(--accent);
  }
  .front__contents { left: 994px; bottom: 25px; font-size: 14.5px; color: var(--ink); line-height: 17px; }
  .count {
    left: 1058px; bottom: 25px; color: var(--paper); font-size: 17px; font-weight: 800; line-height: 22px;
    display: flex; align-items: center; gap: 4px;
  }
  .count__badge {
    writing-mode: horizontal-tb; transform: rotate(-90deg);
    width: 21px; height: 21px; border-radius: 50%; background: var(--paper); color: var(--tone);
    font-size: 11px; line-height: 21px; text-align: center;
  }
</style>
</head>
<body>

<section class="band band--indica">
  <div class="band__edge"></div>
  <span class="vertical blank__label">BLANK SPACE</span>
  <div class="seam"></div>
  <span class="vertical back__brand">PELLET CO</span>
  <div class="back__molecule" role="img" aria-label="THC molecule structure diagram"></div>
  <p class="vertical back__notice">FOR ADULT USE ONLY.<br>KEEP AWAY FROM CHILDREN.</p>
  <p class="vertical back__disclaimer">This product has not been analyzed<br>or evaluated by the NRB</p>
  <div class="back__rule back__rule--a"></div>
  <p class="vertical back__ingredients">Ingredients: Olive oil, full spectrum<br>cannabis extract, gelatin capsules</p>
  <div class="back__rule back__rule--b"></div>
  <div class="back__origin-mark" role="img" aria-label="Outline of Washington DC"></div>
  <span class="vertical back__origin">Made in DC</span>
  <div class="fold"></div>
  <div class="front"></div>
  <span class="vertical vertical--up front__brand">PELLET CO</span>
  <p class="vertical vertical--up front__dose">10MG THC<br>PER CAPSULE</p>
  <span class="vertical vertical--up front__strain">INDICA</span>
  <p class="vertical vertical--up front__contents">15 Full Spectrum<br>Cannabis Extract Capsules</p>
  <p class="vertical vertical--up count"><span class="count__badge">15</span>CAPSULES</p>
</section>

<section class="band band--sativa">
  <div class="band__edge"></div>
  <span class="vertical blank__label">BLANK SPACE</span>
  <div class="seam"></div>
  <span class="vertical back__brand">PELLET CO</span>
  <div class="back__molecule" role="img" aria-label="THC molecule structure diagram"></div>
  <p class="vertical back__notice">FOR ADULT USE ONLY.<br>KEEP AWAY FROM CHILDREN.</p>
  <p class="vertical back__disclaimer">This product has not been analyzed<br>or evaluated by the NRB</p>
  <div class="back__rule back__rule--a"></div>
  <p class="vertical back__ingredients">Ingredients: Olive oil, full spectrum<br>cannabis extract, gelatin capsules</p>
  <div class="back__rule back__rule--b"></div>
  <div class="back__origin-mark" role="img" aria-label="Outline of Washington DC"></div>
  <span class="vertical back__origin">Made in DC</span>
  <div class="fold"></div>
  <div class="front"></div>
  <span class="vertical vertical--up front__brand">PELLET CO</span>
  <p class="vertical vertical--up front__dose">10MG THC<br>PER CAPSULE</p>
  <span class="vertical vertical--up front__strain">SATIVA</span>
  <p class="vertical vertical--up front__contents">15 Full Spectrum<br>Cannabis Extract Capsules</p>
  <p class="vertical vertical--up count"><span class="count__badge">15</span>CAPSULES</p>
</section>

<section class="band band--hybrid">
  <div class="band__edge"></div>
  <span class="vertical blank__label">BLANK SPACE</span>
  <div class="seam"></div>
  <span class="vertical back__brand">PELLET CO</span>
  <div class="back__molecule" role="img" aria-label="THC molecule structure diagram"></div>
  <p class="vertical back__notice">FOR ADULT USE ONLY.<br>KEEP AWAY FROM CHILDREN.</p>
  <p class="vertical back__disclaimer">This product has not been analyzed<br>or evaluated by the NRB</p>
  <div class="back__rule back__rule--a"></div>
  <p class="vertical back__ingredients">Ingredients: Olive oil, full spectrum<br>cannabis extract, gelatin capsules</p>
  <div class="back__rule back__rule--b"></div>
  <div class="back__origin-mark" role="img" aria-label="Outline of Washington DC"></div>
  <span class="vertical back__origin">Made in DC</span>
  <div class="fold"></div>
  <div class="front"></div>
  <span class="vertical vertical--up front__brand">PELLET CO</span>
  <p class="vertical vertical--up front__dose">10MG THC<br>PER CAPSULE</p>
  <span class="vertical vertical--up front__strain">HYBRID</span>
  <p class="vertical vertical--up front__contents">15 Full Spectrum<br>Cannabis Extract Capsules</p>
  <p class="vertical vertical--up count"><span class="count__badge">15</span>CAPSULES</p>
</section>

</body>
</html>
```